Salt Water Delivery Company Business Card Design

We are a company that delivers natural saltwater (from the ocean) to aquarium companies, restaurants and home marine tanks. I would like a new business card to suit.

Must include Name, company name, abn, contact number and website as well as logo (see attached).

Looking for a design that stands out, has a clean but unique appearance.

Double and single sided entries welcome

Industry/Entity Type

Business

Requirements
Must have
• Logo

```html
<!DOCTYPE html>
<html lang="en">
<head>
<meta charset="utf-8">
<title>Tideline Seawater Supply – Business Card</title>
<link href="https://fonts.googleapis.com/css2?family=Nunito+Sans:wght@400;600;800&display=swap" rel="stylesheet">
<style>
  :root {
    --page: #e4e6e8;
    --ocean: #1a90d2;
    --ocean-deep: #0d6eb4;
    --brand: #1768ae;
    --accent: #2a93d5;
    --ink: #4a4d52;
    --paper: #ffffff;
    --paper-shade: #eef0f2;
  }
  * { box-sizing: border-box; margin: 0; padding: 0; }
  html, body { width: 1200px; height: 900px; overflow: hidden; }
  body {
    background: var(--page);
    font-family: "Nunito Sans", Arial, sans-serif;
    display: flex;
    flex-direction: column;
    align-items: center;
    justify-content: center;
    gap: 36px;
  }
  .card {
    width: 700px;
    height: 400px;
    border-radius: 4px;
    box-shadow: 0 10px 28px rgba(0,0,0,.18);
    position: relative;
    overflow: hidden;
  }
  /* Back side */
  .card-back {
    background: radial-gradient(ellipse at 55% 45%, var(--ocean) 0%, var(--ocean-deep) 100%);
    display: flex;
    flex-direction: column;
    align-items: center;
    justify-content: center;
    gap: 22px;
    color: #fff;
  }
  .brand {
    display: flex;
    align-items: center;
    gap: 12px;
    font-weight: 800;
    line-height: 1;
  }
  .brand-dot {
    border-radius: 50%;
    flex: none;
  }
  .card-back .brand { font-size: 40px; color: #fff; }
  .card-back .brand-dot { width: 30px; height: 30px; background: #fff; }
  .back-web { font-size: 17px; letter-spacing: .5px; opacity: .9; }

  /* Front side */
  .card-front {
    background: linear-gradient(160deg, var(--paper) 40%, var(--paper-shade) 100%);
    color: var(--ink);
  }
  .card-front .brand {
    position: absolute;
    top: 48px;
    right: 44px;
    font-size: 32px;
    color: var(--brand);
  }
  .card-front .brand-dot { width: 22px; height: 22px; background: var(--accent); }
  .holder { position: absolute; left: 44px; top: 176px; }
  .holder-name { font-size: 26px; font-weight: 400; }
  .holder-role { font-size: 20px; font-weight: 600; color: var(--accent); margin-top: 2px; }
  .contacts { position: absolute; left: 44px; top: 262px; list-style: none; }
  .contacts li {
    display: flex; align-items: center; gap: 14px;
    font-size: 19px; line-height: 27px;
  }
  .contacts svg { width: 16px; height: 16px; fill: var(--accent); flex: none; }
  .abn { position: absolute; left: 44px; top: 352px; font-size: 20px; }
  .abn span { color: var(--accent); font-weight: 600; }
</style>
</head>
<body>
  <section class="card card-back" aria-label="Business card, back">
    <div class="brand"><span class="brand-dot"></span>Tideline Seawater Supply</div>
    <div class="back-web">www.tidelineseawater.com.au</div>
  </section>

  <section class="card card-front" aria-label="Business card, front">
    <div class="brand"><span class="brand-dot"></span>Tideline Seawater Supply</div>
    <div class="holder">
      <div class="holder-name">Marcus Hale</div>
      <div class="holder-role">CEO</div>
    </div>
    <ul class="contacts">
      <li>
        <svg viewBox="0 0 16 16" aria-hidden="true"><path d="M4 1l2.5 3-1.5 2c1 2 3 4 5 5l2-1.5 3 2.5-1.5 2.5C8 16 0 8 1.5 2.5z"/></svg>
        0491570156
      </li>
      <li>
        <svg viewBox="0 0 16 16" aria-hidden="true"><path d="M1 3h14v10H1zM2.5 4.5v.3L8 9l5.5-4.2v-.3zM2.5 6.7v4.8h11V6.7L8 10.9z" fill-rule="evenodd"/></svg>
        marcus@tidelineseawater.com.au
      </li>
      <li>
        <svg viewBox="0 0 16 16" aria-hidden="true"><path d="M8 1a7 7 0 100 14A7 7 0 008 1zm0 1.5c.8 0 1.8 1.6 2.1 4.5H5.9C6.2 4.1 7.2 2.5 8 2.5zM2.6 7h2c.1-1.7.4-3.1 1-4A5.5 5.5 0 002.6 7zm8.8 0h2a5.5 5.5 0 00-3-4c.6.9.9 2.3 1 4zM2.6 9a5.5 5.5 0 003 4c-.6-.9-.9-2.3-1-4zm3.3 0c.3 2.9 1.3 4.5 2.1 4.5s1.8-1.6 2.1-4.5zm5.5 0c-.1 1.7-.4 3.1-1 4a5.5 5.5 0 003-4z"/></svg>
        www.tidelineseawater.com.au
      </li>
    </ul>
    <div class="abn"><span>ABN:</span> 987654321</div>
  </section>
</body>
</html>
```